Baron of Bones mobile game for IOS and Android

We need all screens designed for a multiplayer craps app. Please see the attached document describing features and some similar app styles I am looking for. I have also included the prototype of the app in HTML. We would like the app to be design to be compatible on phones or tablets.

In regards to the prototypes, this is just a general idea of how I'd like the layout. For the most part, all of the elements on each screen should be there but I don't necessarily care that they are in the same position(s) as in the prototype. In fact, I would prefer that you don't just follow this as a guide and think outside the box a bit.

I think it is fine for the initial entry to only contain just a subset of the required screens (just main lobby and game table screen) rather than all designers having to submit a design containing all screens for the full app. The remaining screens can then be finished using the same style in the design handover phase of this project. This will give me an idea of the design you have in mind without extra work to all the non-winning bidders.

If you have any questions about this project, please ask.

Good Luck!

Target Market(s)

Casual gamers

Industry/Entity Type

Games

Font styles to use
Sans Serif

Requirements
Must have
• All of the main screens shown in the prototype in the uploads.
Nice to have
• The additional popup screens described in the document.
Should not have
• Content copied from other apps, images requiring license

```html
<!DOCTYPE html>
<html lang="en">
<head>
<meta charset="utf-8">
<title>Baron of Bones – Friends</title>
<link rel="stylesheet" href="https://fonts.googleapis.com/css2?family=Roboto:wght@400;500;700&display=swap">
<style>
  :root {
    --bg: #070909;
    --header-top: #2a2c2e;
    --header-bottom: #0d0f10;
    --divider: #23272a;
    --text: #ffffff;
    --text-soft: #e6e6e6;
    --ring: #3b3f42;
    --badge-fill: #121415;
    --gold: #f4c027;
    --gold-deep: #d89a12;
    --gift-red: #e0261e;
    --avatar-tone-a: #c48f6e;
    --avatar-tone-b: #6f8a3a;
    --host-tone-a: #e43a35;
    --host-tone-b: #7a4a2c;
  }
  * { box-sizing: border-box; margin: 0; padding: 0; }
  html, body { width: 1200px; height: 676px; overflow: hidden; background: var(--bg); }
  body { font-family: "Roboto", Arial, sans-serif; color: var(--text); }
  .screen { position: relative; width: 1200px; height: 676px; background: var(--bg); overflow: hidden; }

  .status-bar { position: absolute; top: 0; left: 0; width: 100%; height: 30px; font-size: 16px; font-weight: 500; }
  .status-signal { position: absolute; left: 14px; top: 8px; }
  .status-time { position: absolute; left: 0; right: 0; top: 8px; text-align: center; }
  .status-battery { position: absolute; right: 14px; top: 7px; display: flex; align-items: center; gap: 6px; }

  .header {
    position: absolute; top: 0; left: 0; width: 100%; height: 184px;
    background: linear-gradient(var(--header-top), var(--header-bottom));
    border-bottom: 1px solid var(--divider);
  }
  .header-title {
    position: absolute; left: 0; right: 0; top: 78px; text-align: center;
    font-size: 41px; font-weight: 700; letter-spacing: 0.5px;
  }
  .round-button {
    position: absolute; width: 98px; height: 98px; border-radius: 50%;
    background: var(--badge-fill); border: 2px solid var(--ring);
    display: flex; align-items: center; justify-content: center;
    box-shadow: 0 3px 8px rgba(0,0,0,.6);
  }
  .social-button { left: 923px; top: 57px; }
  .social-name { color: var(--gold); font-size: 20px; font-weight: 700; }
  .host-button { left: 1044px; top: 57px; overflow: hidden; }
  .host-figure { width: 100%; height: 100%; background: radial-gradient(circle at 50% 40%, var(--host-tone-b) 0 30%, var(--host-tone-a) 60%, var(--badge-fill) 80%); }
  .host-plus { position: absolute; left: 1122px; top: 74px; }

  .friend-list { position: absolute; top: 210px; left: 0; width: 100%; }
  .friend-row { position: absolute; height: 70px; width: 530px; }
  .friend-avatar {
    position: absolute; left: 0; top: 0; width: 66px; height: 66px; border-radius: 50%;
    border: 2px solid var(--ring);
    background: radial-gradient(circle at 50% 45%, var(--avatar-tone-a) 0 45%, var(--avatar-tone-b) 75%);
  }
  .friend-name { position: absolute; left: 101px; top: 6px; font-size: 25px; font-weight: 700; }
  .friend-level { position: absolute; left: 101px; top: 38px; font-size: 18px; color: var(--text-soft); }
  .gift-button {
    position: absolute; left: 439px; top: -1px; width: 68px; height: 68px; border-radius: 50%;
    background: var(--badge-fill); border: 2px solid var(--ring);
    display: flex; align-items: center; justify-content: center;
  }
  .back-button { position: absolute; left: 36px; top: 594px; }
</style>
</head>
<body>
<main class="screen">
  <div class="header">
    <div class="status-bar">
      <svg class="status-signal" width="88" height="14" viewBox="0 0 88 14">
        <g fill="#fff"><circle cx="5" cy="7" r="4.5"/><circle cx="16" cy="7" r="4.5"/><circle cx="27" cy="7" r="4.5"/><circle cx="38" cy="7" r="4.5"/><circle cx="49" cy="7" r="4.5"/></g>
        <path d="M62 5 a11 11 0 0 1 16 0 l-2 2 a8 8 0 0 0 -12 0z M66 9 a5 5 0 0 1 8 0 l-4 4z" fill="#fff"/>
      </svg>
      <div class="status-time">9:41 AM</div>
      <div class="status-battery">100%
        <svg width="30" height="14" viewBox="0 0 30 14"><rect x="0.5" y="0.5" width="26" height="13" rx="3" fill="none" stroke="#fff"/><rect x="2.5" y="2.5" width="22" height="9" rx="1.5" fill="#fff"/><rect x="27.5" y="4.5" width="2" height="5" fill="#fff"/></svg>
      </div>
    </div>
    <h1 class="header-title">FRIENDS</h1>
    <div class="round-button social-button"><span class="social-name">Linkup</span></div>
    <div class="round-button host-button"><div class="host-figure" role="img" aria-label="Illustrated casino host character inviting friends"></div></div>
    <svg class="host-plus" width="30" height="30" viewBox="0 0 30 30"><path d="M11 0h8v11h11v8H19v11h-8V19H0v-8h11z" fill="var(--gold)"/></svg>
  </div>

  <section class="friend-list">
    <div class="friend-row" style="left:56px;top:0"><div class="friend-avatar" role="img" aria-label="Friend profile photo"></div><div class="friend-name">Friend 1</div><div class="friend-level">Level Indication</div><div class="gift-button"><svg width="44" height="44" viewBox="0 0 44 44"><use href="#gift"/></svg></div></div>
    <div class="friend-row" style="left:56px;top:97px"><div class="friend-avatar" role="img" aria-label="Friend profile photo"></div><div class="friend-name">Friend 2</div><div class="friend-level">Level Indication</div><div class="gift-button"><svg width="44" height="44" viewBox="0 0 44 44"><use href="#gift"/></svg></div></div>
    <div class="friend-row" style="left:56px;top:194px"><div class="friend-avatar" role="img" aria-label="Friend profile photo"></div><div class="friend-name">Friend 3</div><div class="friend-level">Level Indication</div><div class="gift-button"><svg width="44" height="44" viewBox="0 0 44 44"><use href="#gift"/></svg></div></div>
    <div class="friend-row" style="left:56px;top:291px"><div class="friend-avatar" role="img" aria-label="Friend profile photo"></div><div class="friend-name">Friend 4</div><div class="friend-level">Level Indication</div><div class="gift-button"><svg width="44" height="44" viewBox="0 0 44 44"><use href="#gift"/></svg></div></div>
    <div class="friend-row" style="left:620px;top:0"><div class="friend-avatar" role="img" aria-label="Friend profile photo"></div><div class="friend-name">Friend 5</div><div class="friend-level">Level Indication</div><div class="gift-button"><svg width="44" height="44" viewBox="0 0 44 44"><use href="#gift"/></svg></div></div>
    <div class="friend-row" style="left:620px;top:97px"><div class="friend-avatar" role="img" aria-label="Friend profile photo"></div><div class="friend-name">Friend 6</div><div class="friend-level">Level Indication</div><div class="gift-button"><svg width="44" height="44" viewBox="0 0 44 44"><use href="#gift"/></svg></div></div>
    <div class="friend-row" style="left:620px;top:194px"><div class="friend-avatar" role="img" aria-label="Friend profile photo"></div><div class="friend-name">Friend 7</div><div class="friend-level">Level Indication</div><div class="gift-button"><svg width="44" height="44" viewBox="0 0 44 44"><use href="#gift"/></svg></div></div>
    <div class="friend-row" style="left:620px;top:291px"><div class="friend-avatar" role="img" aria-label="Friend profile photo"></div><div class="friend-name">Friend 8</div><div class="friend-level">Level Indication</div><div class="gift-button"><svg width="44" height="44" viewBox="0 0 44 44"><use href="#gift"/></svg></div></div>
  </section>

  <svg class="back-button" width="50" height="40" viewBox="0 0 50 40"><path d="M46 20H6 M22 4 6 20l16 16" fill="none" stroke="var(--gold)" stroke-width="5" stroke-linecap="round" stroke-linejoin="round"/></svg>

  <svg width="0" height="0" style="position:absolute">
    <defs>
      <linearGradient id="giftGold" x1="0" y1="0" x2="0" y2="1"><stop offset="0" stop-color="#ffd24a"/><stop offset="1" stop-color="#e39a14"/></linearGradient>
      <g id="gift">
        <path d="M22 12c-4-8-11-8-11-3 0 3 6 3 11 3zM22 12c4-8 11-8 11-3 0 3-6 3-11 3z" fill="none" stroke="var(--gift-red)" stroke-width="3"/>
        <rect x="5" y="12" width="34" height="9" fill="url(#giftGold)"/>
        <rect x="7" y="22" width="30" height="18" fill="url(#giftGold)"/>
        <rect x="19" y="12" width="6" height="28" fill="var(--gold-deep)"/>
      </g>
    </defs>
  </svg>
</main>
</body>
</html>
```